Street Sign Project - Attract Customers

We need a street sign designed to display out the front of the building. It design will need to be 1800mm wide x 900mm high. We need to show potential customers where we are inviting. Some of the attachments are for inspiration. The sign will be printed on a sheet of aluminum. if you have a good look at our web site which is www.pk-r.com.au you should get a good feeling about the company and what we do.

Target Market(s)

Construction companies, landscaping and civil earth moving companies who may drive past our business

Industry/Entity Type

Building

Font styles to use
Sans Serif

Colors
ffffff
3277b5
000000

Requirements
Must have
• Company logo must be the main focus point
• The number "54" on the sign to show street number (300mm high)
• phone number - (02) 9418 3065
• web address - www.pk-r.com.au
• I have loaded pictures i would like to see used in the sign
Nice to have
• Banner picture as attached
Should not have
• Bright colours. Please use our blue colour where possible

```html
<!DOCTYPE html>
<html lang="en">
<head>
<meta charset="utf-8">
<title>Pulley &amp; Kran Rigging – Street Sign</title>
<link rel="stylesheet" href="https://fonts.googleapis.com/css2?family=Archivo:wght@500;700;800&display=swap">
<style>
  :root {
    --brand-blue: #3277b5;
    --brand-blue-deep: #1f5d96;
    --ink: #000000;
    --paper: #ffffff;
    --backdrop: #e9ecef;
    --photo-a: #8fa3b3;
    --photo-b: #5d6f7d;
  }
  * { box-sizing: border-box; margin: 0; padding: 0; }
  html, body {
    width: 1200px; height: 600px; overflow: hidden;
    background: var(--backdrop);
    font-family: "Archivo", Arial, sans-serif;
  }
  .street-sign {
    position: relative;
    width: 1200px; height: 600px;
    background: var(--paper);
  }
  .brand {
    position: absolute; left: 60px; top: 70px;
    display: flex; align-items: center; gap: 22px;
  }
  .brand-mark {
    width: 54px; height: 54px; background: var(--brand-blue); flex: none;
  }
  .brand-name {
    color: var(--brand-blue);
    font-weight: 800;
    font-size: 64px;
    line-height: 0.98;
    text-transform: uppercase;
    letter-spacing: -0.5px;
  }
  .divider {
    position: absolute; left: 612px; top: 78px;
    width: 2px; height: 196px; background: var(--brand-blue);
  }
  .contact {
    position: absolute; left: 638px; top: 92px;
    color: var(--brand-blue);
  }
  .contact-item + .contact-item { margin-top: 40px; }
  .contact-label {
    font-size: 15px; font-weight: 700; letter-spacing: 1px;
    text-transform: uppercase;
  }
  .contact-value {
    margin-top: 6px; font-size: 20px; font-weight: 500; color: var(--ink);
  }
  .street-number {
    position: absolute; left: 880px; top: 86px;
    display: flex; align-items: center; gap: 22px;
  }
  .hash {
    color: var(--brand-blue); font-size: 96px; font-weight: 800; line-height: 1;
  }
  .number-disc {
    width: 180px; height: 180px; border-radius: 50%;
    background: var(--brand-blue);
    display: flex; align-items: center; justify-content: center;
    color: var(--paper); font-size: 104px; font-weight: 800;
  }
  .rule {
    position: absolute; left: 60px; top: 326px;
    width: 1080px; height: 3px; background: var(--brand-blue);
  }
  .gallery {
    position: absolute; left: 96px; top: 374px;
    display: flex; gap: 14px;
  }
  .gallery-photo {
    width: 122px; height: 158px;
    border: 3px solid var(--brand-blue);
    background: linear-gradient(160deg, var(--photo-a), var(--photo-b));
  }
  .gallery-photo:nth-child(even) {
    background: linear-gradient(200deg, #a9b6bf, #6c7a86);
  }
</style>
</head>
<body>
  <main class="street-sign">
    <div class="brand">
      <span class="brand-mark" aria-hidden="true"></span>
      <h1 class="brand-name">Pulley &amp;<br>Kran<br>Rigging</h1>
    </div>

    <div class="divider" aria-hidden="true"></div>

    <div class="contact">
      <div class="contact-item">
        <p class="contact-label">Phone Number</p>
        <p class="contact-value">(02) 9418 3065</p>
      </div>
      <div class="contact-item">
        <p class="contact-label">Web Address</p>
        <p class="contact-value">www.pk-r.com.au</p>
      </div>
    </div>

    <div class="street-number" aria-label="Street number 54">
      <span class="hash">#</span>
      <span class="number-disc">54</span>
    </div>

    <div class="rule" aria-hidden="true"></div>

    <div class="gallery">
      <div class="gallery-photo" role="img" aria-label="Photo of an inclined conveyor on a building site"></div>
      <div class="gallery-photo" role="img" aria-label="Photo of hoisting equipment beside scaffolding"></div>
      <div class="gallery-photo" role="img" aria-label="Photo of construction materials on site"></div>
      <div class="gallery-photo" role="img" aria-label="Photo of a material hoist mast on a building"></div>
      <div class="gallery-photo" role="img" aria-label="Photo of a conveyor loading rubble"></div>
      <div class="gallery-photo" role="img" aria-label="Photo of a roofline with hoist installation"></div>
    </div>
  </main>
</body>
</html>
```